Wordpress Template für Weinkommunikation
Zielgruppe
Kunden und potentielle Kunden, die sich über meine Dienstleistungen und mich informieren wollen.
Meine Arbeitsschwerpunkte sind Kommunikation, PR und Events im Weinbereich.
Meine persönlichen Wein-Schwerpunktländer sind Spanien und Portugal. Die Kunden sind von dort, meine Arbeit ist in Deutschland.
Aufgabenstellung
Ich möchte meine bestehende Website endlich mal richtig gestalten lassen.
- Startseite soll statisch sein.
- Weitere Seiten sollen auch statisch möglich sein.
- 2- oder 3-spaltig
- Template muss Widget-fähig sein
- Möglichkeit der Zweisprachigkeit

```html
<!DOCTYPE html>
<html lang="de">
<head>
<meta charset="utf-8">
<title>Traube &amp; Kunde – Weinkommunikation</title>
<link href="https://fonts.googleapis.com/css2?family=Kalam:wght@700&family=Open+Sans:wght@400;600&display=swap" rel="stylesheet">
<style>
:root{
  --bg-dark:#8a6a3c;
  --bg-light:#c9ad7c;
  --paper:#ffffff;
  --side:#efecd8;
  --side-border:#e0dcc3;
  --wine:#6b1c07;
  --wine-dark:#4a1404;
  --nav-top:#7a3512;
  --nav-bottom:#4e1a06;
  --text:#222;
  --link:#3fb6e0;
  --footer-text:#e8d6c2;
  --rule:#c8b98f;
}
*{margin:0;padding:0;box-sizing:border-box}
html,body{width:1199px;height:1200px;overflow:hidden}
body{background:linear-gradient(90deg,var(--bg-dark) 0%,var(--bg-light) 9%,#d7c19a 50%,var(--bg-light) 91%,var(--bg-dark) 100%);font-family:Arial,Helvetica,sans-serif;color:var(--text)}
.page{position:absolute;left:0;top:0;width:999px;height:1000px;transform:scale(1.2);transform-origin:0 0}
.abs{position:absolute}
.hand{font-family:'Kalam',cursive;font-weight:700}

.sheet{left:97px;top:0;width:810px;height:987px;background:var(--paper)}
.brand{left:132px;top:22px;display:flex;align-items:center;gap:12px}
.brand-dot{width:60px;height:60px;border-radius:50%;background:#b8201a}
.brand-name{font-family:'Kalam',cursive;font-weight:700;font-size:30px;line-height:30px;color:#111}

.social{left:663px;top:0;width:236px;height:36px;background:var(--side);border:1px solid var(--side-border);display:flex;justify-content:center;align-items:center;gap:9px}
.social span{width:19px;height:19px;border-radius:4px;background:#8d8a78}

.nav{left:85px;top:112px;width:833px;height:41px;background:linear-gradient(var(--nav-top),var(--nav-bottom));font-family:'Open Sans',sans-serif;font-weight:600;font-size:12px;color:#fff}
.nav a{position:absolute;top:13px;line-height:16px;color:#fff;text-decoration:none;white-space:nowrap}
.hero{left:97px;top:153px;width:566px;height:129px;background:linear-gradient(90deg,#050302 0%,#1a0f08 40%,#5a3b22 70%,#2b1a0e 100%)}
.hero-title{left:130px;top:198px;font-size:24px;color:#fff}

.sidebar{left:666px;top:70px;width:232px;height:860px;background:var(--side);border:4px solid #fff;outline:1px solid var(--side-border)}
.side-h{font-size:18px;color:var(--wine)}
.side-rule{position:absolute;left:676px;width:210px;height:1px;background:linear-gradient(90deg,transparent,var(--rule),transparent)}
.search{left:675px;top:121px;width:160px;height:20px;border:1px solid #a08c6a;background:#fff}
.bottle{left:684px;top:220px;width:22px;height:98px;border-radius:6px 6px 3px 3px;background:linear-gradient(#3a1c12,#1a0a06)}
.feed-box{left:694px;top:288px;width:27px;height:27px;border-radius:5px;background:#e8782a}
.small{font-size:10px;line-height:12px}
.more{font-size:13px;color:var(--wine);text-decoration:underline}
.tweets{left:679px;top:398px;width:205px;font-size:11px;line-height:13px}
.tweets b{color:var(--link);font-weight:bold}
.follow-badge{left:678px;top:505px;width:94px;height:62px;border-radius:8px;background:linear-gradient(#9fd8ef,#e3cf97)}
.mail{left:681px;top:669px;width:165px;height:23px;border:1px solid #8c7b57;background:#fff;font-size:11px;padding:5px 6px}
.badge{border-radius:6px}

.welcome-photo{left:128px;top:313px;width:197px;height:109px;border:1px solid #999;background:linear-gradient(#7fb0dc 0%,#b9d4ea 45%,#5f8f3c 60%,#9db86a 100%)}
.welcome-h{left:340px;top:302px;font-size:16px;color:var(--wine)}
.lead{left:340px;top:332px;width:296px;font-size:10.5px;line-height:13px;font-weight:bold;letter-spacing:-0.2px;hyphens:auto;-webkit-hyphens:auto}
.body-text{left:126px;width:510px;font-size:11px;line-height:13px;hyphens:auto;-webkit-hyphens:auto}
.videos-h{left:126px;top:586px;font-size:16px;color:var(--wine)}

.clip{background:var(--wine);border-radius:3px;box-shadow:0 8px 10px rgba(0,0,0,.15)}
.clip .shot{position:absolute;left:3px;top:3px;right:3px;background:linear-gradient(#5f8c3a,#c2d89a 50%,#87a64f)}
.caption{left:277px;top:771px;width:204px;height:26px;background:rgba(255,255,255,.8);text-align:center;font-family:'Open Sans',sans-serif;font-weight:600;font-size:12px;line-height:26px;color:var(--wine)}

.footer{left:97px;top:848px;width:810px;height:139px;background:linear-gradient(#6b2208,#4a1604)}
.footer-col{top:853px}
.footer-col h3{font-family:'Kalam',cursive;font-weight:700;font-size:21px;color:#ecd9c8;line-height:30px}
.footer-col a{display:block;font-family:'Open Sans',sans-serif;font-size:11px;line-height:18px;color:var(--footer-text);text-decoration:none}
</style>
</head>
<body>
<div class="page">
  <div class="abs sheet"></div>

  <div class="abs brand">
    <span class="brand-dot"></span>
    <span class="brand-name">Traube &amp; Kunde<br>Jens K. Varga</span>
  </div>

  <div class="abs social" aria-label="Soziale Netzwerke">
    <span></span><span></span><span></span><span></span><span></span><span></span><span></span>
  </div>

  <nav class="abs nav">
    <a href="#" style="left:26px">Home</a>
    <a href="#" style="left:88px">Wer</a>
    <a href="#" style="left:144px">Referenzen</a>
    <a href="#" style="left:238px">Buchtipps</a>
    <a href="#" style="left:329px">Wein-News</a>
    <a href="#" style="left:426px">Wein-Glossar</a>
    <a href="#" style="left:531px">Blog</a>
  </nav>

  <div class="abs hero" role="img" aria-label="Fotografie von Holzfässern in einem Weinkeller"></div>
  <div class="abs hero-title hand">Weinkommunkation</div>

  <aside class="abs sidebar"></aside>
  <div class="abs side-h hand" style="left:676px;top:92px">Suche</div>
  <div class="abs search"></div>
  <div class="side-rule" style="top:160px"></div>

  <div class="abs side-h hand" style="left:676px;top:180px">BlogNews</div>
  <div class="abs bottle" role="img" aria-label="Weinflasche"></div>
  <div class="abs feed-box"></div>
  <div class="abs" style="left:718px;top:227px;font-size:13px;line-height:15px;font-weight:bold;color:#333">Aus der Weinwelt von<br>Traube &amp; Kunde ...</div>
  <div class="abs small" style="left:718px;top:261px;font-weight:bold;color:#333">blog.traube-kunde.de - mein Blog<br>mit Infos, News und mehr.</div>
  <div class="abs more hand" style="left:802px;top:294px">mehr Info´s</div>
  <div class="side-rule" style="top:352px"></div>

  <div class="abs side-h hand" style="left:678px;top:364px">Follow Me</div>
  <div class="abs tweets">
    <p><b>@kellerfreund</b> Wann können wir das Ergebnis verkosten? <b>#riesling</b></p><br>
    <p>Last call! Anmeldefrist zu Sommelier Cup 2010 endet in wenigen Tagen <b>kurz.link/8f2m</b>... Den Siegern winken Fortbildungs-Stipendien!</p>
  </div>
  <div class="abs follow-badge" role="img" aria-label="Illustration eines Vogels mit Follow-Schild"></div>
  <div class="abs more hand" style="left:802px;top:534px">follow me</div>
  <div class="side-rule" style="top:592px"></div>

  <div class="abs side-h hand" style="left:681px;top:608px">Newsletter anmelden</div>
  <div class="abs" style="left:682px;top:636px;font-size:11px;line-height:13px;width:180px">Hier können Sie sich zum Newsletter anmelden.</div>
  <div class="abs mail">E-Mail Adresse eingeben</div>
  <div class="side-rule" style="top:712px"></div>

  <div class="abs badge" style="left:677px;top:731px;width:205px;height:43px;background:linear-gradient(#fff,#d7d7d2);border:1px solid #ccc"></div>
  <div class="abs badge" style="left:723px;top:797px;width:101px;height:32px;background:#d9d3c0"></div>
  <div class="abs badge" style="left:721px;top:867px;width:110px;height:32px;background:linear-gradient(#f3f3f3,#cfd6df);border:1px solid #aab"></div>

  <div class="abs welcome-photo" role="img" aria-label="Porträtfoto vor Weinbergen"></div>
  <div class="abs welcome-h hand">Herzlich Willkommen bie Traube&amp;Kunde</div>
  <p class="abs lead">Mit Traube &amp; Kunde möchte ich Ihnen vor allem mein Wissen über Wein - insbesondere der Iberischen Halbinsel - über die Weinbau-Länder, die unterschiedlichen Regionen, die abwechslungsreichen Landschaften, die unzähligen Kellereien, die Winzerpersönlichkeiten, aber auch meine ganz persönlichen Eindrücke und Erlebnisse zur Kultur, zur Gastronomie,</p>
  <p class="abs body-text" style="top:434px">zu den Menschen und zum Leben in Spanien, Portugal, der Weinwelt und zum Thema Genuss allgemein zugänglich machen.</p>
  <p class="abs body-text" style="top:473px">Durch die langjährige Erfahrung im internationalen Weingrosshandel und der Weinszene sind die Bereiche Kommunikation, PR und Marketing, sowie die Sortiments- und Einkaufsberatung, neben den Schulungen ein wichtiger Bestandteil des Angebotes.<br>Speziell im institutionellen Bereich biete ich Verbänden, Regionen und Ländern die Möglichkeit, sich über den deutschen Weinmarkt kundig zu machen, zu eruieren wo und wie sie ihre Produkte am sinnvollsten anbieten können. Hierzu gehört auch die Kommunikations- und Pressearbeit, sowie die Konzeption, Planung und Durchführung von Veranstaltungen.</p>

  <div class="abs videos-h hand">Wein Videos bei Traube &amp; Kunde</div>

  <div class="abs clip" style="left:199px;top:669px;width:78px;height:114px"><div class="shot" role="img" aria-label="Videostandbild mit Weinflaschen" style="height:100px"></div></div>
  <div class="abs clip" style="left:481px;top:669px;width:65px;height:114px"><div class="shot" role="img" aria-label="Videostandbild mit Weinflaschen" style="height:100px"></div></div>
  <div class="abs clip" style="left:273px;top:641px;width:211px;height:178px"><div class="shot" role="img" aria-label="Videostandbild mit Weinglas und Weinflaschen im Weinberg" style="height:154px"></div></div>
  <div class="abs caption">Wein Wissen für Anfänger</div>
  <svg class="abs" style="left:284px;top:802px" width="190" height="12" aria-hidden="true"><polygon points="0,1 0,11 8,6" fill="#fff"/><rect x="20" y="5" width="168" height="2" fill="#d8b9a8"/></svg>

  <footer class="abs footer"></footer>
  <div class="abs footer-col" style="left:125px"><h3>Links</h3><a>Impressum</a><a>Kontakt</a><a>AGB</a><a>Sitemap</a><a>Datenschutz</a></div>
  <div class="abs footer-col" style="left:265px"><h3>Service</h3><a>Wein Knigge</a><a>Weintouren</a><a>Weinwissen</a></div>
  <div class="abs footer-col" style="left:415px"><h3>Wein-News</h3><a>&nbsp;Lange Nächte der Weinkeller</a><a>Winzer relativ zufrieden</a><a>Erste-Lage-Spätlesen im Rampenlicht</a><a>Neue Sommelier-Ausbildung</a></div>
</div>
</body>
</html>
```